Tasman Curdworks Guild needs new business cards

We need new business cards designed and produced. We are likely to need other design work done for ads, flyers etc in future.

We would like to start with an initial business card.

The Tasman Curdworks Guild (TCG) is a membership-based not-for-profit organisation that looks after the interests of Australia's small to medium artisan cheesemakers, many of whom are also small-scale farmers. The design should be simple, using our logo, but also communicate our artisan cheese and small dairy farm focus.

The first card to be designed and produced is for me, Miriam Tolhurst. My details are:

Miriam Tolhurst
Secretary
Tasman Curdworks Guild (TCG)
http://www.curdworksguild.example
T +61452837190
E miriam.miriamtolhurst@mailbox.example

I have attached the TCG logo in jpg form. I have a higher resolution version available if needed.

Thank you!

Miriam

Miriam Tolhurst
Tasman Curdworks Guild
miriam.miriamtolhurst@mailbox.example
+61452837190

Sans Serif

• Logo (see attached file)

```html
<!DOCTYPE html>
<html lang="en">
<head>
<meta charset="utf-8">
<title>Tasman Curdworks Guild — Business Card</title>
<link rel="stylesheet" href="https://fonts.googleapis.com/css2?family=Cormorant+Garamond:wght@500&family=Open+Sans:wght@400&display=swap">
<style>
  :root {
    --page: #ffffff;
    --card: #e27633;
    --ink: #ffffff;
  }
  html, body {
    margin: 0;
    padding: 0;
    width: 1200px;
    height: 767px;
    overflow: hidden;
    background: var(--page);
  }
  .canvas {
    position: relative;
    width: 1200px;
    height: 767px;
  }
  .card {
    position: absolute;
    left: 57px;
    top: 73px;
    width: 1050px;
    height: 600px;
    border-radius: 46px;
    background: var(--card);
  }
  .card-frame {
    position: absolute;
    left: 0;
    top: 0;
  }
  .identity {
    position: absolute;
    left: 140px;
    top: 202px;
    color: var(--ink);
    margin: 0;
  }
  .person-name {
    font-family: "Cormorant Garamond", serif;
    font-weight: 500;
    font-size: 44px;
    letter-spacing: 4px;
    text-transform: uppercase;
    line-height: 1;
  }
  .person-role {
    font-family: "Open Sans", sans-serif;
    font-size: 24px;
    letter-spacing: 0;
    text-transform: none;
  }
  .organisation {
    font-family: "Open Sans", sans-serif;
    font-size: 24px;
    margin-top: 8px;
    line-height: 1.2;
  }
  .contacts {
    position: absolute;
    left: 209px;
    top: 344px;
    margin: 0;
    padding: 0;
    list-style: none;
    font-family: "Open Sans", sans-serif;
    font-size: 24px;
    color: var(--ink);
  }
  .contacts li {
    display: flex;
    align-items: center;
    height: 41.5px;
  }
  .contacts svg {
    width: 36px;
    height: 36px;
    margin-right: 8px;
    flex: none;
  }
  .guild-mark {
    position: absolute;
    left: 660px;
    top: 465px;
    display: flex;
    align-items: center;
    color: var(--ink);
  }
  .guild-mark-circle {
    width: 132px;
    height: 132px;
    border: 2px solid var(--ink);
    border-radius: 50%;
    margin-right: 28px;
    box-sizing: border-box;
  }
  .guild-mark-name {
    font-family: "Cormorant Garamond", serif;
    font-weight: 500;
    font-size: 34px;
    line-height: 38px;
    letter-spacing: 1px;
  }
</style>
</head>
<body>
<main class="canvas">
  <section class="card" aria-label="Business card">
    <svg class="card-frame" width="1050" height="600" viewBox="57 73 1050 600" aria-hidden="true">
      <path d="M145 104 H1018 A57 57 0 0 0 1075 161 V580 A57 57 0 0 0 1018 637 H145 A57 57 0 0 0 90 580 V161 A57 57 0 0 0 145 104 Z"
            fill="none" stroke="#ffffff" stroke-width="3.5" stroke-dasharray="10 7"/>
    </svg>
  </section>

  <header class="identity">
    <div class="person-name">Miriam Tolhurst,<span class="person-role"> Secretary</span></div>
    <div class="organisation">Tasman Curdworks Guild (TCG)</div>
  </header>

  <ul class="contacts">
    <li>
      <svg viewBox="0 0 36 36" aria-hidden="true">
        <circle cx="18" cy="18" r="16.5" fill="none" stroke="#fff" stroke-width="2"/>
        <path d="M11.5 9.5 l4 -1 l2 5 l-2.5 2 c1.2 2.6 3 4.4 5.5 5.5 l2 -2.5 l5 2 l-1 4 c-8 1 -16 -7 -15 -15 z" fill="#fff"/>
      </svg>
      miriam.miriamtolhurst@mailbox.example
    </li>
    <li>
      <svg viewBox="0 0 36 36" aria-hidden="true">
        <circle cx="18" cy="18" r="16.5" fill="none" stroke="#fff" stroke-width="2"/>
        <rect x="8.5" y="11" width="19" height="14" fill="none" stroke="#fff" stroke-width="2"/>
        <path d="M8.5 11 L18 19 L27.5 11 M8.5 25 L15 18.5 M27.5 25 L21 18.5" fill="none" stroke="#fff" stroke-width="1.8"/>
      </svg>
      +61452837190
    </li>
    <li>
      <svg viewBox="0 0 36 36" aria-hidden="true">
        <circle cx="18" cy="18" r="16.5" fill="none" stroke="#fff" stroke-width="2"/>
        <circle cx="18" cy="18" r="11" fill="none" stroke="#fff" stroke-width="1.6"/>
        <ellipse cx="18" cy="18" rx="5" ry="11" fill="none" stroke="#fff" stroke-width="1.6"/>
        <path d="M7 18 H29 M9 12.5 H27 M9 23.5 H27" fill="none" stroke="#fff" stroke-width="1.6"/>
      </svg>
      http://www.curdworksguild.example
    </li>
  </ul>

  <div class="guild-mark">
    <div class="guild-mark-circle" aria-hidden="true"></div>
    <div class="guild-mark-name">Tasman<br>Curdworks<br>Guild</div>
  </div>
</main>
</body>
</html>
```